Business card with professional look

I would like a creative yet professional looking business card for our business. We sell broadcast TV related security products for mobile phones, set top boxes, and tablets. Our customers are international. We have a logo we like and I would like to possibly add some color to the business card but keep it professional looking.

Target Market(s)

Professionals in the TV, cable, ans Satellite industries

Industry/Entity Type

Cable Tv

Contact Information for Business Card

Name Ned Vastermill, title CEO, Address 8130 Harborline Court, Suite 400, Del Arvo, CA 91584 USA, phone numbers m:+1.619.284.7302 o:+1.855.672.9140, email, logo

Font styles to use
Other font styles liked:
• Open to any font that looks good with logo

Requirements
Must have
• professional look with colors coordinated with logo colors. would like to add one or two different colors as well as some form of background color

```html
<!DOCTYPE html>
<html lang="en">
<head>
<meta charset="utf-8">
<title>Vaultcast — Business Card</title>
<link rel="stylesheet" href="https://fonts.googleapis.com/css2?family=Open+Sans:wght@300;400;700&display=swap">
<style>
  :root {
    --backdrop: #d9d4cc;
    --card: #f7f7f7;
    --card-edge: #ececec;
    --band: #4a4a4c;
    --band-text: #f2f2f2;
    --ink: #555558;
    --ink-soft: #6a6a6d;
    --accent: #1f8fd6;
    --rule: #b9b9bb;
  }
  * { box-sizing: border-box; margin: 0; padding: 0; }
  html, body {
    width: 1200px; height: 892px; overflow: hidden;
    background: var(--backdrop);
    font-family: "Open Sans", Arial, sans-serif;
  }
  .card {
    position: absolute; left: 100px; top: 160px;
    width: 1000px; height: 571px;
    background: linear-gradient(135deg, #ffffff 0%, var(--card) 55%, var(--card-edge) 100%);
    box-shadow: 0 14px 30px rgba(0,0,0,0.25);
    overflow: hidden;
  }
  .brand {
    position: absolute; left: 70px; top: 170px;
    width: 340px; height: 120px;
    display: flex; align-items: center; gap: 16px;
  }
  .brand-mark {
    width: 58px; height: 58px; border-radius: 10px;
    background: var(--accent); flex: none;
  }
  .brand-name {
    font-weight: 700; font-size: 54px; letter-spacing: -1.5px;
    color: var(--ink);
  }
  .divider {
    position: absolute; left: 470px; top: 50px;
    width: 1px; height: 370px; background: var(--rule);
  }
  .person { position: absolute; left: 530px; top: 70px; }
  .person-name {
    font-weight: 300; font-size: 42px; color: var(--ink); line-height: 1.15;
  }
  .person-title {
    font-weight: 300; font-size: 30px; color: var(--accent); line-height: 1.2;
  }
  .contacts {
    position: absolute; left: 530px; top: 230px;
    list-style: none;
  }
  .contact {
    display: flex; align-items: center; gap: 22px;
    height: 56px;
    font-weight: 300; font-size: 29px; color: var(--ink-soft);
  }
  .contact-icon { width: 30px; height: 30px; flex: none; }
  .address-band {
    position: absolute; left: 0; bottom: 0;
    width: 100%; height: 112px;
    background: var(--band);
    display: flex; align-items: center; justify-content: center;
    color: var(--band-text); font-size: 31px; font-weight: 400; letter-spacing: -0.3px;
  }
</style>
</head>
<body>
  <div class="card">
    <div class="brand">
      <span class="brand-mark"></span>
      <span class="brand-name">Vaultcast</span>
    </div>

    <div class="divider"></div>

    <div class="person">
      <p class="person-name">Ned Vastermill</p>
      <p class="person-title">CEO</p>
    </div>

    <ul class="contacts">
      <li class="contact">
        <svg class="contact-icon" viewBox="0 0 30 30" aria-hidden="true">
          <rect x="1" y="1" width="28" height="28" rx="2" fill="#58585b"/>
          <path d="M8 12c0-3 3-4 7-4s7 1 7 4l-3 1-1-2h-6l-1 2z" fill="#fff"/>
          <rect x="9" y="15" width="12" height="7" rx="1" fill="#fff"/>
        </svg>
        <span>+1.855.672.9140</span>
      </li>
      <li class="contact">
        <svg class="contact-icon" viewBox="0 0 30 30" aria-hidden="true">
          <rect x="1" y="1" width="28" height="28" rx="2" fill="#58585b"/>
          <rect x="7" y="7" width="16" height="16" rx="2" fill="none" stroke="#fff" stroke-width="2.5"/>
        </svg>
        <span>+1.619.284.7302</span>
      </li>
      <li class="contact">
        <svg class="contact-icon" viewBox="0 0 30 30" aria-hidden="true">
          <rect x="1" y="1" width="28" height="28" rx="2" fill="#58585b"/>
          <rect x="6" y="9" width="18" height="12" fill="none" stroke="#fff" stroke-width="2"/>
          <path d="M6 9l9 7 9-7" fill="none" stroke="#fff" stroke-width="2"/>
        </svg>
        <span>ned@vaultcastmail.com</span>
      </li>
    </ul>

    <div class="address-band">
      8130 Harborline Court, Suite 400, Del Arvo, CA 91584 USA
    </div>
  </div>
</body>
</html>
```